Modern and Sleek Non-Fiction Book Cover Design

Seeking a talented graphic designer to create a modern and sleek cover and back page for a book to be published on Pagewick . The design should be visually appealing and align with the book's theme, using bright colors to make it stand out. The title is "The Counsel Office Welcome Manual" with "The" in a smaller font, and the tagline "Intake as a Competitive Advantage" should be included. The book is targeted at an audience interested in immigration and family law firms. So I would like it on the cover as well. The hex numbers for the colors are 00aeeef, fcb034, and 336a89. The cover should feature the author's photo prominently.
-Design a modern front cover for the book
-Design a sleek back page for the book
-Ensure designs meet Pagewick publishing requirements 8x5 paperback
Let's not use the side image, it doesn't seem to fit like I thought it might.

```html
<!DOCTYPE html>
<html lang="en">
<head>
<meta charset="utf-8">
<title>The Counsel Office Welcome Manual — Cover Spread</title>
<link rel="stylesheet" href="https://fonts.googleapis.com/css2?family=Cormorant+Garamond:wght@600;700&family=Source+Serif+4:wght@300;400&display=swap">
<style>
  :root {
    --amber: #fbb034;
    --navy: #002a40;
    --white: #ffffff;
    --photo-dark: #4a2c26;
    --photo-mid: #7a4a3c;
    --photo-light: #c9a08a;
  }
  html, body {
    margin: 0;
    padding: 0;
    width: 1200px;
    height: 914px;
    overflow: hidden;
    background: var(--amber);
  }
  .spread {
    position: relative;
    width: 1200px;
    height: 914px;
    background: var(--amber);
    font-family: "Source Serif 4", Georgia, serif;
  }

  /* Back cover */
  .back-copy {
    position: absolute;
    left: 54px;
    top: 90px;
    width: 467px;
    margin: 0;
    color: var(--navy);
    font-size: 16.2px;
    line-height: 19.6px;
    font-weight: 300;
    text-align: justify;
    hyphens: auto;
  }
  .back-copy p { margin: 0 0 19.6px; }
  .back-copy p.clipped {
    height: 255px;
    overflow: hidden;
    margin: 0;
  }
  .isbn-box {
    position: absolute;
    left: 296px;
    top: 772px;
    width: 219px;
    height: 104px;
    background: var(--white);
  }

  /* Spine */
  .spine {
    position: absolute;
    left: 568px;
    top: 0;
    width: 64px;
    height: 914px;
    background: var(--navy);
  }
  .spine-title, .spine-author {
    position: absolute;
    left: 50%;
    color: var(--white);
    white-space: nowrap;
    transform-origin: 0 0;
    font-weight: 300;
  }
  .spine-title {
    top: 108px;
    font-size: 22px;
    transform: rotate(90deg) translateY(-50%);
  }
  .spine-author {
    top: 642px;
    font-size: 20px;
    transform: rotate(90deg) translateY(-50%);
  }

  /* Front cover */
  .author-photo {
    position: absolute;
    left: 713px;
    top: 8px;
    width: 365px;
    height: 490px;
  }
  .title-panel {
    position: absolute;
    left: 677px;
    top: 470px;
    width: 474px;
    height: 368px;
    background: var(--navy);
  }
  .title-art {
    position: absolute;
    left: 677px;
    top: 460px;
    width: 474px;
    height: 378px;
    overflow: visible;
  }
  .title-art text {
    font-family: "Cormorant Garamond", "Times New Roman", serif;
    font-weight: 700;
  }
  .tagline {
    position: absolute;
    left: 677px;
    top: 774px;
    width: 474px;
    margin: 0;
    text-align: center;
    color: var(--white);
    font-size: 27px;
    font-weight: 400;
  }
  .author-name {
    position: absolute;
    left: 677px;
    top: 862px;
    width: 474px;
    margin: 0;
    text-align: center;
    color: var(--navy);
    font-size: 26px;
    letter-spacing: 0.32em;
    font-weight: 400;
  }
</style>
</head>
<body>
<main class="spread">

  <section class="back-cover">
    <div class="back-copy">
      <p>Lorem ipsum dolor sit amet, consectetur adipisicing elit, sed do eiusmod tempor incididunt ut labore et dolore magna aliqua. Ut enim ad minim veniam, quis nostrud exercitation ullamco laboris nisi ut aliquip ex ea commodo consequat. Duis aute irure dolor in reprehenderit in voluptate velit esse cillum dolore eu fugiat nulla pariatur. Excepteur sint occaecat cupidatat non proident, sunt in culpa qui officia deserunt mollit anim id est laborum. Sed ut perspiciatis unde omnis iste natus error sit voluptatem accusantium doloremque laudantium, totam rem aperiam, eaque ipsa quae ab illo inventore veritatis et quasi architecto beatae vitae dicta sunt explicabo. Nemo enim ipsam voluptatem quia voluptas sit aspernatur aut odit aut fugit, sed quia consequuntur magni dolores eos qui ratione voluptatem sequi nesciunt. Neque porro quisquam est, qui dolorem ipsum quia dolor sit amet, consectetur, adipisci velit, sed quia non numquam eius modi tempora incidunt ut labore et dolore magnam aliquam quaerat voluptatem.</p>
      <p class="clipped">Lorem ipsum dolor sit amet, consectetur adipisicing elit, sed do eiusmod tempor incididunt ut labore et dolore magna aliqua. Ut enim ad minim veniam, quis nostrud exercitation ullamco laboris nisi ut aliquip ex ea commodo consequat. Duis aute irure dolor in reprehenderit in voluptate velit esse cillum dolore eu fugiat nulla pariatur. Excepteur sint occaecat cupidatat non proident, sunt in culpa qui officia deserunt mollit anim id est laborum. Sed ut perspiciatis unde omnis iste natus error sit voluptatem accusantium doloremque laudantium, totam rem aperiam, eaque ipsa quae ab illo inventore veritatis et quasi architecto beatae vitae dicta sunt explicabo. Nemo enim ipsam voluptatem quia voluptas sit aspernatur aut odit aut fugit, sed quia consequuntur magni dolores eos qui ratione voluptatem sequi nesciunt. Neque porro quisquam est, qui dolorem ipsum quia dolor sit amet.</p>
    </div>
    <div class="isbn-box"></div>
  </section>

  <section class="spine">
    <span class="spine-title">The Counsel Office Welcome Manual</span>
    <span class="spine-author">AUTHOR NAME</span>
  </section>

  <section class="front-cover">
    <svg class="author-photo" viewBox="0 0 365 490" role="img" aria-label="Author portrait: smiling man in glasses and a brown plaid blazer, leaning forward with hands clasped">
      <defs>
        <linearGradient id="portraitTone" x1="0" y1="0" x2="0" y2="1">
          <stop offset="0" stop-color="var(--photo-light)"/>
          <stop offset="0.35" stop-color="var(--photo-mid)"/>
          <stop offset="1" stop-color="var(--photo-dark)"/>
        </linearGradient>
      </defs>
      <path d="M130 20 Q180 -5 230 20 L240 120 Q320 140 345 230 L360 410 Q340 470 300 490 L60 490 Q20 470 0 400 L20 220 Q40 140 125 120 Z" fill="url(#portraitTone)"/>
    </svg>

    <div class="title-panel"></div>

    <svg class="title-art" viewBox="0 0 474 378" aria-label="The Counsel Office Welcome Manual">
      <text x="20" y="68" font-size="72" fill="var(--white)">The</text>
      <text x="20" y="139" font-size="58" fill="var(--amber)" textLength="434" lengthAdjust="spacingAndGlyphs">COUNSEL OFFICE</text>
      <text x="20" y="222" font-size="90" fill="var(--white)" textLength="436" lengthAdjust="spacingAndGlyphs">WELCOME</text>
      <text x="20" y="300" font-size="82" fill="var(--amber)" textLength="434" lengthAdjust="spacingAndGlyphs">MANUAL</text>
    </svg>

    <p class="tagline">Intake as a Competitive Advantage</p>
    <p class="author-name">AUTHOR NAME</p>
  </section>

</main>
</body>
</html>
```